Bespoke Branding Agency "Tidal Marks" seeks uplifting wordpress site

Looking for a SIMPLE, CLEAN, easy to manage wordpress site for our start-up Branding business. Our company is "Tidal Marks" and the site should reflect our vision.

We formed the company after making the decision never to work the average 9 to 5 work life again. We have vowed to never work in traditional corporate culture again. We are committed to a happier life with reduced stress and increased job satisfaction.

We want to build brands that make people happy.

We want to work with people who believe that you don’t have to be an asshole to be successful.

We believe that success should not be measured in monetary terms, but rather in happiness scores.

We believe in the Corwin Ashdale song lyric "Folks ought to grin often”.

We love sunflowers.

We prefer brevity over long wind.

We are motivated by creativity not money.

We love spending time with friends and family, and see this as our main priority in life.

We know life is short.

Industry/Entity Type

Business

```html
<!DOCTYPE html>
<html lang="en">
<head>
<meta charset="utf-8">
<title>Tidal Marks</title>
<link rel="stylesheet" href="https://fonts.googleapis.com/css2?family=Raleway:wght@300;400&family=Open+Sans:wght@400&family=Fira+Sans+Extra+Condensed:wght@600&display=swap">
<style>
:root{
  --header-bg:#474b55;
  --footer-bg:#2b221c;
  --brand-yellow:#fdb515;
  --nav-text:#f2f2f2;
  --card-bg:rgba(38,34,22,0.78);
  --card-line:#e6d9a6;
  --tan:#d9c894;
  --muted:#b9b2a8;
  --white:#ffffff;
  --sky-top:#8fb4e6;
  --sky-mid:#a9c6ea;
  --field-top:#e7c21a;
  --field-bottom:#7a6a14;
}
*{box-sizing:border-box;margin:0;padding:0}
html,body{width:1200px;height:859px;overflow:hidden;background:var(--footer-bg)}
body{position:relative;font-family:"Open Sans",sans-serif}
.site-header{position:absolute;left:0;top:0;width:1200px;height:84px;background:var(--header-bg);z-index:2}
.brand{position:absolute;left:99px;top:0;height:84px;display:flex;align-items:center;gap:12px}
.brand-dot{width:18px;height:18px;border-radius:50%;background:var(--brand-yellow)}
.brand-name{font-family:"Raleway",sans-serif;font-weight:400;font-size:22px;color:var(--nav-text)}
.main-nav{position:absolute;right:99px;top:29px;display:flex;align-items:center;gap:35px}
.main-nav a{font-family:"Raleway",sans-serif;font-size:15px;color:var(--nav-text);text-decoration:none;letter-spacing:.3px}
.menu-toggle{width:29px;height:25px;border:1.5px solid #d8d8d8;border-radius:4px;display:flex;align-items:center;justify-content:center}
.hero{position:absolute;left:0;top:84px;width:1200px;height:676px}
.hero-photo{position:absolute;inset:0;background:linear-gradient(180deg,var(--sky-top) 0%,var(--sky-mid) 50%,var(--field-top) 60%,#d9a812 78%,var(--field-bottom) 100%)}
.hero-arrow{position:absolute;top:289px;width:34px;height:34px;border-radius:50%;background:rgba(110,118,130,.8);display:flex;align-items:center;justify-content:center}
.hero-arrow.prev{left:55px}
.hero-arrow.next{left:1118px}
.hero-title{position:absolute;right:115px;top:286px;text-align:right;font-family:"Fira Sans Extra Condensed",sans-serif;font-weight:600;color:var(--white);text-shadow:0 0 2px #f3b90f,0 0 2px #f3b90f,1px 1px 0 #e9a90c}
.hero-title .line-main{display:block;font-size:64px;line-height:66px;letter-spacing:.5px}
.hero-title .line-sub{display:block;font-size:42px;line-height:50px}
.feature-row{position:absolute;left:99px;top:500px;display:flex;gap:28px}
.feature-card{width:315px;height:146px;background:var(--card-bg);position:relative}
.feature-icon{position:absolute;left:31px;top:30px;width:86px;height:86px;border:1.5px solid var(--card-line);border-radius:50%;display:flex;align-items:center;justify-content:center}
.feature-title{position:absolute;left:141px;top:21px;font-family:"Raleway",sans-serif;font-weight:300;font-size:22px;color:var(--white)}
.feature-text{position:absolute;left:141px;top:57px;font-size:11.5px;line-height:20.5px;color:var(--white)}
.site-footer{position:absolute;left:0;top:760px;width:1200px;height:99px;background:var(--footer-bg)}
.footer-block{position:absolute;top:26px}
.footer-heading{font-family:"Raleway",sans-serif;font-weight:400;font-size:19px;color:var(--tan);letter-spacing:.3px}
.footer-text{font-size:12px;color:var(--muted);margin-top:4px}
.footer-social{position:absolute;left:843px;top:34px;display:flex;align-items:center}
.footer-social .footer-heading{margin-right:20px}
.social-dot{width:28px;height:28px;border-radius:50%;background:#3a2f27;border:1px solid #4e4238;margin-right:4px}
</style>
</head>
<body>
<header class="site-header">
  <div class="brand"><span class="brand-dot"></span><span class="brand-name">Tidal Marks</span></div>
  <nav class="main-nav">
    <a href="#">HOME</a>
    <a href="#">ABOUT US</a>
    <a href="#">TIDAL MARKS</a>
    <a href="#">CONTACT US</a>
    <span class="menu-toggle"><svg width="15" height="13" viewBox="0 0 15 13"><rect y="0" width="15" height="2.6" rx="1" fill="#e5e5e5"/><rect y="5.2" width="15" height="2.6" rx="1" fill="#e5e5e5"/><rect y="10.4" width="15" height="2.6" rx="1" fill="#e5e5e5"/></svg></span>
  </nav>
</header>

<section class="hero">
  <div class="hero-photo" role="img" aria-label="Woman with raised arms standing in a sunflower field under a blue sky"></div>
  <span class="hero-arrow prev"><svg width="12" height="18" viewBox="0 0 12 18"><path d="M9 2 2 9l7 7" fill="none" stroke="#fff" stroke-width="2"/></svg></span>
  <span class="hero-arrow next"><svg width="12" height="18" viewBox="0 0 12 18"><path d="M3 2l7 7-7 7" fill="none" stroke="#fff" stroke-width="2"/></svg></span>
  <h1 class="hero-title"><span class="line-main">FOLKS OUGHT TO</span><span class="line-sub">Grin Often</span></h1>

  <div class="feature-row">
    <article class="feature-card">
      <span class="feature-icon"><svg width="34" height="38" viewBox="0 0 34 38" fill="#e6d9a6"><path d="M16 36V12h2v24z"/><ellipse cx="17" cy="6" rx="3.5" ry="6"/><ellipse cx="9" cy="16" rx="7" ry="3.5" transform="rotate(35 9 16)"/><ellipse cx="25" cy="16" rx="7" ry="3.5" transform="rotate(-35 25 16)"/><ellipse cx="9" cy="26" rx="7" ry="3.5" transform="rotate(35 9 26)"/><ellipse cx="25" cy="26" rx="7" ry="3.5" transform="rotate(-35 25 26)"/></svg></span>
      <h2 class="feature-title">What We Do</h2>
      <p class="feature-text">Lorem ipsum dolor sit amet,<br>consectetuer adipiscing elit.<br>Lorem ipsum Lorem</p>
    </article>
    <article class="feature-card">
      <span class="feature-icon"><svg width="40" height="34" viewBox="0 0 40 34" fill="#e6d9a6"><rect x="2" y="11" width="9" height="11" rx="1"/><path d="M11 11 30 3v27L11 22z"/><rect x="31" y="12" width="5" height="9" rx="2"/><path d="M5 22h6l2 10H8z"/></svg></span>
      <h2 class="feature-title">Tidal Marks</h2>
      <p class="feature-text">Lorem ipsum dolor sit amet,<br>consectetuer adipiscing elit.<br>Lorem ipsum Lorem</p>
    </article>
    <article class="feature-card">
      <span class="feature-icon"><svg width="38" height="28" viewBox="0 0 38 28"><rect x="1.5" y="1.5" width="35" height="25" rx="2" fill="none" stroke="#e6d9a6" stroke-width="3"/><path d="M2 3l17 13L36 3" fill="none" stroke="#e6d9a6" stroke-width="3"/></svg></span>
      <h2 class="feature-title">How To Find Us</h2>
      <p class="feature-text">Lorem ipsum dolor sit amet,<br>consectetuer adipiscing elit.<br>Lorem ipsum Lorem</p>
    </article>
  </div>
</section>

<footer class="site-footer">
  <div class="footer-block" style="left:99px">
    <h3 class="footer-heading">COPYRIGHT</h3>
    <p class="footer-text">(c) 2015 Tidal Marks. All rights reserved.</p>
  </div>
  <div class="footer-block" style="left:459px">
    <h3 class="footer-heading">ADDRESS</h3>
    <p class="footer-text">9870 Harbour Row, Leith, LH 45 TM 45</p>
  </div>
  <div class="footer-social">
    <h3 class="footer-heading">FOLLOW US</h3>
    <span class="social-dot"></span><span class="social-dot"></span><span class="social-dot"></span><span class="social-dot"></span>
  </div>
</footer>
</body>
</html>
```